Elegant, Playful, Health And Wellness Packaging Design for an Essential Oil Diffuser

Box design for diffuser, should be elegant, luxury, white box with gold foil and vibrant color combination that pops off the white box.

Designs look the same

```html
<!DOCTYPE html>
<html lang="en">
<head>
<meta charset="utf-8">
<title>Aurelle Diffuser Box – Dieline</title>
<link href="https://fonts.googleapis.com/css2?family=Cinzel:wght@400;600&display=swap" rel="stylesheet">
<style>
  :root {
    --backdrop: #4d4d4d;
    --board: #ffffff;
    --gold: #c59a35;
    --gold-deep: #b78a2a;
    --gold-light: #ecd57a;
    --ink: #3a3a3a;
    --crease: #9a9a9a;
  }
  html, body {
    margin: 0;
    padding: 0;
    width: 1200px;
    height: 444px;
    overflow: hidden;
    background: var(--backdrop);
  }
  .dieline {
    display: block;
    width: 1200px;
    height: 444px;
  }
  .board { fill: var(--board); }
  .foil-panel { fill: url(#foil); }
  .crease { stroke: var(--crease); stroke-width: 1.5; fill: none; }
  .type {
    font-family: "Cinzel", serif;
    font-weight: 400;
    letter-spacing: 0.04em;
  }
  .tagline { fill: var(--gold); font-size: 10px; }
  .product-line { fill: var(--gold-deep); font-size: 10px; font-weight: 600; }
  .collection { fill: var(--ink); font-size: 11px; }
  .brand-name { fill: var(--gold); font-size: 30px; font-weight: 600; letter-spacing: 0.08em; }
  .brand-name--lid { font-size: 44px; }
  .brand-dot { fill: var(--gold); }
  .side-copy { fill: #ffffff; font-size: 14px; }
  .web-address { fill: var(--ink); font-size: 11px; }
</style>
</head>
<body>
<svg class="dieline" viewBox="646 70 2216 820" xmlns="http://www.w3.org/2000/svg" role="img" aria-label="Flat dieline of the Aurelle diffuser box">
  <defs>
    <linearGradient id="foil" x1="0" y1="0" x2="1" y2="1">
      <stop offset="0" stop-color="#d3a73f"/>
      <stop offset="0.45" stop-color="#dcb650"/>
      <stop offset="0.7" stop-color="#ecd57a"/>
      <stop offset="1" stop-color="#d6ad46"/>
    </linearGradient>
  </defs>

  <!-- Left side panel -->
  <g class="side-panel side-panel--left">
    <path class="foil-panel" role="img" aria-label="Gold foil side panel with faint ornamental medallion"
      d="M1121,400 L1160,280 Q1165,268 1178,268 L1415,268 Q1428,268 1430,280 L1437,425 L1437,676 L1121,676 Z"/>
    <path class="board" d="M1121,676 L1437,676 L1280,755 L1280,820 Q1280,835 1265,835 L1135,835 Q1121,835 1121,820 Z"/>
    <text class="type side-copy" x="1275" y="551">ESSENTIAL OIL</text>
    <text class="type side-copy" x="1275" y="567">AROMA DIFFUSER</text>
  </g>

  <!-- Front panel with lid -->
  <g class="front-panel">
    <path class="board" d="M1437,427 L1437,100 Q1437,77 1460,77 L1731,77 Q1754,77 1754,100 L1754,427 Z"/>
    <line class="crease" x1="1437" y1="110" x2="1754" y2="110"/>
    <text class="type brand-name brand-name--lid" x="1596" y="282" text-anchor="middle">AURELLE</text>

    <rect class="board" x="1437" y="427" width="317" height="249"/>
    <line class="crease" x1="1437" y1="427" x2="1754" y2="427"/>
    <text class="type tagline" x="1596" y="451" text-anchor="middle">EXPERIENCE THE ESSENCE OF NATURE</text>
    <circle class="brand-dot" cx="1596" cy="522" r="20"/>
    <text class="type brand-name" x="1596" y="584" text-anchor="middle">AURELLE</text>
    <text class="type collection" x="1596" y="602" text-anchor="middle">SIGNATURE RARE OILS COLLECTION</text>
    <text class="type product-line" x="1596" y="656" text-anchor="middle">ESSENTIAL OIL AROMA DIFFUSER</text>

    <path class="board" d="M1437,676 L1754,676 L1754,870 Q1754,880 1744,880 L1676,880 L1676,835 L1517,835 L1517,880 L1447,880 Q1437,880 1437,870 Z"/>
    <line class="crease" x1="1437" y1="676" x2="1754" y2="676"/>
    <text class="type web-address" x="1598" y="767" text-anchor="middle">WWW.AURELLE-OILS.COM</text>
  </g>

  <!-- Right side panel -->
  <g class="side-panel side-panel--right">
    <path class="foil-panel" role="img" aria-label="Gold foil side panel with faint ornamental medallion"
      d="M1754,425 L1760,280 Q1762,268 1775,268 L2020,268 Q2032,268 2036,280 L2070,400 L2070,676 L1754,676 Z"/>
    <path class="board" d="M1754,676 L2070,676 L2070,820 Q2070,835 2055,835 L1925,835 Q1912,835 1912,820 L1912,755 Z"/>
    <text class="type side-copy" x="1860" y="552" text-anchor="middle">EXPERIENCE THE</text>
    <text class="type side-copy" x="1850" y="567" text-anchor="middle">ESSENCE OF NATURE</text>
  </g>

  <!-- Back panel -->
  <g class="back-panel">
    <path class="board" d="M2183,427 L2183,402 Q2183,392 2193,392 L2267,392 Q2277,392 2277,402 L2277,427 Z"/>
    <rect class="board" x="2070" y="427" width="318" height="249"/>
    <text class="type tagline" x="2223" y="451" text-anchor="middle">EXPERIENCE THE ESSENCE OF NATURE</text>
    <circle class="brand-dot" cx="2228" cy="522" r="20"/>
    <text class="type brand-name" x="2228" y="584" text-anchor="middle">AURELLE</text>
    <text class="type collection" x="2228" y="602" text-anchor="middle">SIGNATURE RARE OILS COLLECTION</text>
    <text class="type product-line" x="2228" y="656" text-anchor="middle">ESSENTIAL OIL AROMA DIFFUSER</text>
    <path class="board" d="M2070,676 L2388,676 L2308,835 L2308,868 Q2308,880 2296,880 L2160,880 Q2148,880 2148,868 L2148,835 Z"/>
    <line class="crease" x1="2070" y1="676" x2="2388" y2="676"/>
  </g>
</svg>
</body>
</html>
```